2020-23 Strategic Plan - Graphic Design Work

We would would like to have our strategic plan designed. It should be two pages.

- I am looking for suggestions on ways to lay this out. I don’t like this boxy layout. It was great for the committee as we went through multiple versions, but I’d prefer the final not follow this boxy format

- I’ve included a few images we own (feel free to use any or none of them). Also attached our logo.

- Have a look at our new website to see our new branding look and feel (launching next week) https://thevorlex.plinthweb.com/

- I've included a copy of our logo.

Target Market(s)

Membership

Other font styles liked:
• Lato

Requirements
Must have
• Excellent layout. Easy to ready. Consistent with branding.

```html
<!DOCTYPE html>
<html lang="en">
<head>
<meta charset="utf-8">
<title>VIV 2020-2023 Strategic Plan</title>
<link href="https://fonts.googleapis.com/css2?family=Lato:wght@300;400;700;900&family=Montserrat:wght@600;700;800&display=swap" rel="stylesheet">
<style>
  :root{
    --stage:#d6d6d6;
    --paper:#e4e4e4;
    --green-deep:#163d1a;
    --green:#2f6f2b;
    --green-bright:#3f9a38;
    --ink:#3a3a3a;
    --rule:#9a9a9a;
    --white:#ffffff;
  }
  *{box-sizing:border-box;margin:0;padding:0}
  html,body{width:1200px;height:900px;overflow:hidden;background:var(--stage)}
  body{font-family:"Lato",sans-serif;color:var(--ink);display:flex;align-items:center;justify-content:center;gap:16px}
  .page{position:relative;width:584px;height:452px;background:var(--paper);overflow:hidden;box-shadow:0 6px 18px rgba(0,0,0,.18)}

  /* Page one */
  .hero-photo{position:absolute;left:0;top:0;width:178px;height:100%;
    background:linear-gradient(160deg,var(--green-deep) 0%,var(--green) 45%,var(--green-bright) 80%,var(--green) 100%)}
  .brand{position:absolute;left:14px;top:56px;width:150px;color:var(--white);text-align:center}
  .brand-mark{display:flex;align-items:center;justify-content:center;gap:7px}
  .brand-square{width:16px;height:16px;background:var(--white)}
  .brand-name{font-family:"Lato",sans-serif;font-weight:900;font-size:34px;letter-spacing:1px;line-height:1}
  .brand-full{font-family:"Lato",sans-serif;font-weight:900;font-size:7px;letter-spacing:.4px;margin-top:4px;border-bottom:1px solid var(--white);padding-bottom:3px;white-space:nowrap}
  .section-rule{position:absolute;left:0;height:1px;background:var(--white)}
  .plan-heading{position:absolute;left:200px;top:38px;color:var(--green-deep)}
  .plan-years{font-family:"Lato",sans-serif;font-weight:300;font-size:30px;line-height:1}
  .plan-title{font-family:"Montserrat",sans-serif;font-weight:800;font-size:30px;line-height:1.05}
  .intro{position:absolute;top:122px;width:170px;font-size:6.6px;line-height:1.55}
  .intro.one{left:200px}.intro.two{left:384px}
  .statement{position:absolute;left:210px;width:350px}
  .statement h2{font-family:"Montserrat",sans-serif;font-weight:700;font-size:10px;letter-spacing:.5px;color:var(--green-deep);margin-bottom:5px}
  .statement p{font-size:6.8px;line-height:1.55}

  /* Page two */
  .side-strip{position:absolute;left:0;top:0;width:30px;height:100%;background:var(--green)}
  .side-photo{position:absolute;left:0;bottom:0;width:30px;height:150px;
    background:linear-gradient(180deg,var(--green) 0%,var(--green-deep) 100%)}
  .strip-tick{position:absolute;left:0;width:30px;height:1px;background:var(--white)}
  .plan-table{position:absolute;left:46px;top:34px;width:524px}
  .table-head,.table-row{display:grid;grid-template-columns:80px 120px 148px 1fr}
  .table-head{background:var(--green-bright);color:var(--white);
    font-family:"Montserrat",sans-serif;font-weight:700;font-size:6px;letter-spacing:.3px;padding:5px 6px;white-space:nowrap}
  .table-row{padding:12px 6px;border-bottom:1px dotted var(--rule);min-height:92px;align-items:start}
  .pillar{font-family:"Montserrat",sans-serif;font-weight:800;font-size:8px;color:var(--green-deep);align-self:center}
  .objective,.goals p,.actions li{font-size:6.2px;line-height:1.45;padding-right:8px}
  .goals p{margin-bottom:5px}
  .actions{list-style:none}
  .actions li{position:relative;padding-left:7px;margin-bottom:3px}
  .actions li::before{content:"";position:absolute;left:0;top:3px;width:2.5px;height:2.5px;border-radius:50%;background:var(--ink)}
</style>
</head>
<body>

<section class="page plan-overview">
  <div class="hero-photo" role="img" aria-label="Green-toned photo of city towers seen from below"></div>
  <div class="brand">
    <div class="brand-mark"><span class="brand-square"></span><span class="brand-name">VIV</span></div>
    <div class="brand-full">VORLEX INSTITUTE OF VALUATION</div>
  </div>
  <span class="section-rule" style="top:206px;width:178px"></span>
  <span class="section-rule" style="top:262px;width:178px"></span>
  <span class="section-rule" style="top:324px;width:178px"></span>

  <div class="plan-heading">
    <div class="plan-years">2020-2023</div>
    <div class="plan-title">STRATEGIC PLAN</div>
  </div>
  <p class="intro one">With over 980 members, the Vorlex Institute of Valuation is the region's leading association of property assessment and taxation professionals. Our diverse membership is comprised of individuals from the private and public sectors practicing in the fields of assessment, consultancy, appraisal, taxation and law.</p>
  <p class="intro two">Incorporated in March 1964, the VIV is dedicated to advancing the interests, education and professional competence of its members. Our members are highly qualified and widely recognized as the leading professionals in the property assessment industry.</p>

  <div class="statement" style="top:212px">
    <h2>VISION</h2>
    <p>To be the industry leader in education, ethical standards, and professional accreditation in the field of property assessment in our region.</p>
  </div>
  <div class="statement" style="top:268px">
    <h2>MISSION</h2>
    <p>To provide specialized education through a comprehensive approach to training which embraces all available technologies. To promote professional development and to ensure our members are recognized as experts in the field of property assessment and related functions.</p>
  </div>
  <div class="statement" style="top:334px">
    <h2>VALUES</h2>
    <p>The Vorlex Institute of Valuation and its members value professionalism, inclusivity, diversity, integrity, ethics, accountability, and expertise. The VIV is committed to serving all members and stakeholders with competence and respect, rejecting all forms of prejudice and discrimination.</p>
  </div>
</section>

<section class="page plan-pillars">
  <div class="side-strip"></div>
  <div class="side-photo" role="img" aria-label="Green-toned photo of a glass tower facade"></div>
  <span class="strip-tick" style="top:132px"></span>
  <span class="strip-tick" style="top:226px"></span>
  <span class="strip-tick" style="top:320px"></span>
  <span class="strip-tick" style="top:412px"></span>

  <div class="plan-table">
    <div class="table-head"><span>STRATEGIC PILLAR</span><span>STRATEGIC OBJECTIVE</span><span>STRATEGIC GOALS</span><span></span></div>

    <div class="table-row">
      <span class="pillar">EDUCATE</span>
      <p class="objective">Be the most trusted, relevant, and accessible provider of education and credentials in the field of property assessment in our region</p>
      <div class="goals">
        <p>Ensure a catalogue of relevant, high-quality courses which meet the evolving needs of assessment professionals</p>
        <p>Provide an equal VIV member experience and service, regardless of geography</p>
        <p>Enhance opportunities for senior assessment professionals through the FVIV designation.</p>
      </div>
      <ul class="actions">
        <li>Update course content on a regular review cycle</li>
        <li>Develop provincial legislation courses</li>
        <li>Lead opportunities for collaboration across districts to increase access to quality PD opportunities</li>
        <li>Develop framework for a specialist designation track</li>
      </ul>
    </div>

    <div class="table-row">
      <span class="pillar">GROW</span>
      <p class="objective">Increase the VIV's membership by serving all career levels and forging strong strategic partnerships.</p>
      <div class="goals">
        <p>Connect with young professionals by enhancing member communications, improving member onboarding, and expanding scholarship opportunities.</p>
      </div>
      <ul class="actions">
        <li>Work collaboratively with strategic partners from across the region to develop criteria for, and launch, the FVIV designation</li>
        <li>Redesign the new member onboarding experience</li>
      </ul>
    </div>

    <div class="table-row">
      <span class="pillar">LEAD</span>
      <p class="objective">Strengthen the reputation of the organization and its members by acting as a leader within the field of property assessment in our region</p>
      <div class="goals">
        <p>Embrace the role of leader and advocate within the property assessment profession</p>
        <p>Strengthen current, and develop new, strategic partnerships with peer associations across the region.</p>
      </div>
      <ul class="actions">
        <li>Adopt an advocacy voice for the assessment profession to ensure interests are being represented</li>
        <li>Work with strategic partners to produce industry white papers with wide relevance</li>
        <li>Engage with various levels of government across the region</li>
      </ul>
    </div>

    <div class="table-row">
      <span class="pillar">GOVERN</span>
      <p class="objective">Fortify the future of the VIV through operational excellence and a diverse group of talented volunteers</p>
      <div class="goals">
        <p>Review and align association management practices with strategic objectives and statements of Vision, Mission and Values.</p>
        <p>Secure the VIV's financial stability by reviewing current pricing model and practicing sound risk management.</p>
      </div>
      <ul class="actions">
        <li>Align the VIV budget and staffing needs to achieve clear strategic objectives</li>
        <li>Utilize automation to modernize systems and administrative processes</li>
        <li>Review and assess the relevance of current committees to determine if sufficient to meet the requirements of the strategic plan, and create new committees if deemed relevant</li>
      </ul>
    </div>
  </div>
</section>

</body>
</html>
```